Website redesign: OLU - Bright Reel Studio

Web Design Brief
I'm looking for a redesign of our website https://www.brightreel.studio/. The website is built with Wix.

We are an AI Video Production Agency named OLU that uses AI-technology to create videos for our clients. We use the platform vormetric.io to generate videos.

Use case:
A financial services company is looking for a way to transform their inhouse training content to video.
They visit brightreel.studio and submit a brief.
Several production packages are presented, and the company selects the one that suits them best. Pricing is agreed upon, and the company provides the necessary scripts and documentation.

As a growing agency, our web page's primary objective is to acquire business leads (companies seeking professional video services) and to communicate our unique AI-driven approach to video production. The landing page will include a form for potential clients to fill out their requirements, as well as a showcase of our AI's capabilities in video production.

We have not yet chosen a color palette, but we are looking for a design that will inspire confidence in our clients while also highlighting the innovative and creative nature of our service. The overall theme should be sleek, modern, and visual, as our core offering is video creation and editing.

Current website:
https://www.brightreel.studio/

Competitors:
https://www.clipforge.pro/
https://pixelbound.ai/
https://www.quillspots.com/vormetric

Inspiration:
https://www.vormetric.io/
https://lumo.co.uk/
https://crispnorth.co/
https://www.bluefennel.com/

Target Market(s)

Director's of training and others who work with video at companies with $10M+ in revenue and 100+ employees.

Industry/Entity Type

Video Services Agency

Coding

Coded - Design and coding required

Number of Pages Required

1 page

Font styles to use
Sans Serif

Requirements
Must have
• Clear CTA and services showcase above the fold. Include "Services" and "Blog" section.
Nice to have
• Reviews / Proof of concept

```html
<!DOCTYPE html>
<html lang="en">
<head>
<meta charset="utf-8">
<title>OLU - Bright Reel Studio</title>
<link href="https://fonts.googleapis.com/css2?family=Montserrat:wght@400;500;600;700;800&display=swap" rel="stylesheet">
<style>
:root{
  --blue:#1a6fe8;
  --blue-deep:#1f4fd6;
  --cyan:#12b4f2;
  --sky:#e6f5fd;
  --ink:#111;
  --body:#3b3b3b;
  --muted:#777;
  --card:#fff;
  --card-grey:#eef1f8;
  --field:#fff;
}
*{margin:0;padding:0;box-sizing:border-box}
html,body{width:1200px;height:5098px;overflow:hidden}
body{position:relative;font-family:'Montserrat',sans-serif;color:var(--ink);background:#fff}
.abs{position:absolute}
.eyebrow{font-size:15px;font-weight:700;color:var(--blue);letter-spacing:.5px}
.h2{font-size:36px;font-weight:800;letter-spacing:1px;line-height:1.05}
.center{text-align:center;left:0;width:1200px}
.brand{display:flex;align-items:center;gap:12px;color:#fff;font-weight:800;font-size:44px;letter-spacing:2px}
.brand .dot{width:56px;height:56px;border-radius:50%;border:4px solid #fff}
.btn-pill{display:inline-flex;align-items:center;justify-content:center;border-radius:22px;font-weight:700;font-size:14px}
.ph{border-radius:14px}

/* hero */
.hero{left:0;top:0;width:1200px;height:520px;background:linear-gradient(120deg,#1a3fa8 0%,#1f5fd8 55%,#1d6bea 100%)}
.nav{left:540px;top:32px;display:flex;gap:0;color:#fff;font-size:13px;font-weight:600}
.nav span{margin-right:32px}
.hero h1{left:163px;top:175px;color:#fff;font-size:55px;font-weight:800;line-height:62px;letter-spacing:1px}
.hero .sub{left:165px;top:302px;color:#fff;font-size:17px;font-weight:500;line-height:30px;letter-spacing:.5px}
.hero .btn-pill{left:163px;top:383px;width:172px;height:40px;background:var(--cyan);color:#fff}
.hero-video{left:570px;top:140px;width:506px;height:312px;border:8px solid #cfe0ff;border-radius:16px;background:linear-gradient(135deg,#2a3550,#5a6a90 50%,#1c2540)}

/* about */
.about-img1{left:325px;top:650px;width:260px;height:212px;background:linear-gradient(135deg,#153a78,#4aa3e0)}
.about-circle{left:150px;top:765px;width:255px;height:255px;border-radius:50%;border:8px solid #f1f3f7;background:linear-gradient(135deg,#7a8a9a,#c8d3de);box-shadow:0 6px 18px rgba(0,0,0,.15)}
.about-img2{left:422px;top:883px;width:147px;height:152px;background:linear-gradient(135deg,#9a8a7a,#d9d2c9)}
.about-text{left:620px;top:643px;width:420px}
.about-text p{font-size:13px;line-height:24.5px;color:var(--body);margin-top:14px}
.about-text .btn-pill{margin-top:22px;width:120px;height:42px;background:var(--blue);color:#fff}

/* services */
.band-sky{left:0;top:1095px;width:1200px;height:830px;background:var(--sky);clip-path:polygon(0 110px,1200px 0,1200px 100%,0 100%)}
.svc-card{top:1377px;width:282px;height:288px;background:var(--card);border-radius:10px;text-align:center;padding:90px 22px 0}
.svc-card h3{font-size:17px;font-weight:600;line-height:23px}
.svc-card p{font-size:12.5px;line-height:25px;color:var(--body);margin-top:12px}
.svc-icon{top:1325px;width:104px;height:104px;border-radius:50%;display:flex;align-items:center;justify-content:center}
.arrow{width:42px;height:20px}

/* benefits */
.band-blue{left:0;top:1805px;width:1200px;height:650px;background:linear-gradient(90deg,#19b0f2 0%,#1d8ef0 45%,#2a63e6 100%);clip-path:polygon(0 70px,1200px 0,1200px 555px,0 645px)}
.mid-mark{left:518px;top:1733px;width:164px;height:164px;border-radius:50%;background:#fff;border:7px solid #e8f2ff;box-shadow:0 6px 20px rgba(0,0,0,.15);display:flex;align-items:center;justify-content:center}
.mid-mark span{width:112px;height:112px;border-radius:50%;background:linear-gradient(135deg,#1ab3f3,#1f5fd8)}
.benefit{width:420px;color:#fff}
.benefit .kick{font-size:15px;font-weight:700;letter-spacing:.5px}
.benefit h3{font-size:38px;font-weight:800;letter-spacing:1px;margin-top:2px}
.benefit p{font-size:12.5px;line-height:25px;margin-top:12px}
.benefit li{font-size:12.5px;line-height:25px;margin-top:10px;list-style:none;padding-left:25px;position:relative}
.benefit li::before{content:"";position:absolute;left:3px;top:10px;width:6px;height:6px;border-radius:50%;background:#fff}
.benefit .btn-pill{margin-top:22px;width:143px;height:38px;border:1.5px solid #fff;color:#fff;font-weight:600}
.vid{top:2250px;width:415px;height:256px;border:7px solid #eef4fb;border-radius:10px}
.play{position:absolute;right:16px;top:14px;width:30px;height:30px;border:2px solid #fff;border-radius:50%}
.play::after{content:"";position:absolute;left:10px;top:7px;border-left:9px solid #fff;border-top:6px solid transparent;border-bottom:6px solid transparent}

/* why */
.why-card{top:2722px;width:282px;height:288px;background:var(--card-grey);border-radius:10px;padding:36px 24px 0}
.why-card h3{font-size:17px;font-weight:600;line-height:24px;margin-top:16px}
.why-card p{font-size:12.5px;line-height:25px;color:var(--body);margin-top:14px}

/* reviews */
.band-review{left:0;top:3080px;width:1200px;height:580px;background:var(--sky);clip-path:polygon(0 100px,1200px 0,1200px 470px,0 100%)}
.quote{left:560px;top:3318px;font-size:130px;font-weight:800;color:var(--blue);line-height:1}
.review-text{left:300px;top:3385px;width:600px;font-size:13px;line-height:25px;color:var(--body);text-align:center}

/* blog */
.post{top:3812px;border-radius:10px;overflow:hidden}
.post span{position:absolute;left:20px;bottom:20px;color:#fff;font-size:14px;font-weight:500;line-height:18px}

/* contact */
.band-foot{left:0;top:4270px;width:1200px;height:828px;background:linear-gradient(90deg,#1a9ff0,#1e62e2)}
.contact-card{left:162px;top:4235px;width:876px;height:475px;background:#e4f4fc;border-radius:8px;overflow:hidden}
.contact-deco{position:absolute;right:-40px;top:20px;width:360px;height:440px;border-radius:50%;background:linear-gradient(135deg,#2a8df0,#1f4fd6);opacity:.9}
.field{position:absolute;background:var(--field);border-radius:22px;font-size:12px;color:#333;padding:12px 28px}
.field b{color:#e33;font-weight:500}
.submit{left:208px;top:4640px;width:118px;height:36px;background:var(--blue);color:#fff;font-size:13px}

/* footer */
.foot-nav{left:0;width:1200px;top:4905px;display:flex;justify-content:center;gap:0;color:#fff;font-size:13px}
.foot-nav span{margin:0 35px}
.foot-info{top:4955px;color:#fff;font-size:12.5px;line-height:24px;display:flex;gap:16px;align-items:flex-start}
.rule{left:162px;top:5040px;width:876px;height:1px;background:rgba(255,255,255,.35)}
</style>
</head>
<body>

<!-- HERO -->
<section class="abs hero">
  <div class="abs brand" style="left:162px;top:12px">
    <span class="dot"></span>OLU
  </div>
  <nav class="abs nav"><span>Training</span><span>Marketing</span><span>How ?</span><span>Services</span><span>Blogs</span><span>Contact Us</span></nav>
  <h1 class="abs">GROW YOUR<br>BUSINESS</h1>
  <p class="abs sub">By Improving Operations Efficiency<br>Through Video Powered By AI</p>
  <a class="abs btn-pill">LEARN MORE &nbsp;→</a>
  <div class="abs hero-video" role="img" aria-label="AI presenter speaking in front of a night city skyline"></div>
</section>

<!-- ABOUT -->
<div class="abs about-img1 ph" role="img" aria-label="Person wearing a VR headset in a blue-lit office"></div>
<div class="abs about-circle" role="img" aria-label="Team collaborating in a modern studio"></div>
<div class="abs about-img2 ph" role="img" aria-label="Smiling production team standing together"></div>
<div class="abs about-text">
  <div class="eyebrow">ABOUT</div>
  <h2 class="h2" style="font-size:38px;margin-top:2px">BRIGHT REEL STUDIO</h2>
  <p>OLU levels up your training and marketing teams thanks to high-quality and efficient video production powered by AI. You will combine the latest technology available with the most professional and human touch.</p>
  <p style="margin-top:6px">It is not just about video, it is about a digital strategy. You may want to create a website such as this one, growing your traffic with SEO, or finding new clients using pay advertisement on different platforms such as LinkNet, FaceBoard, Snapframe &amp; Chirper. it will all depend on where your customers are... and yes, we are here to support you.</p>
  <a class="btn-pill">Read More</a>
</div>

<!-- SERVICES -->
<div class="abs band-sky"></div>
<div class="abs eyebrow center" style="top:1233px">WHAT WE DO</div>
<h2 class="abs h2 center" style="top:1255px">OUR SERVICES</h2>
<svg class="abs arrow" style="left:100px;top:1510px" viewBox="0 0 42 20"><path d="M41 10H2M10 2 2 10l8 8" fill="none" stroke="#1a6fe8" stroke-width="2"/></svg>
<svg class="abs arrow" style="left:1057px;top:1510px" viewBox="0 0 42 20"><path d="M1 10h39M32 2l8 8-8 8" fill="none" stroke="#1a6fe8" stroke-width="2"/></svg>

<div class="abs svc-card" style="left:162px"><h3>AI Enhanced Website<br>Creation</h3><p>Your Webmaster will be working with you to create your dream website or targeted landing pages that will increase your sales.</p></div>
<div class="abs svc-card" style="left:458px"><h3>AI Enhanced<br>SEO</h3><p>Your SEO will find, target, and measure the results of the keywords using the latest AI SEO tools in the market that will level up your website visitors.</p></div>
<div class="abs svc-card" style="left:756px"><h3>AI Enhanced Social<br>Media</h3><p style="color:var(--muted)">Your Social Media Manager will be posting content, connecting with your audience, and targeting perfect ads to grow your potential customers.</p></div>

<div class="abs svc-icon" style="left:251px;background:var(--blue)"><svg width="56" height="56" viewBox="0 0 56 56" fill="none" stroke="#fff" stroke-width="2"><rect x="8" y="10" width="40" height="34" rx="3"/><path d="M8 17h40"/><circle cx="28" cy="31" r="8"/></svg></div>
<div class="abs svc-icon" style="left:547px;background:var(--cyan)"><svg width="56" height="56" viewBox="0 0 56 56" fill="none" stroke="#fff" stroke-width="2"><circle cx="28" cy="24" r="12"/><path d="M28 36v14M22 50h12M28 6v4M10 24h4M42 24h4"/></svg></div>
<div class="abs svc-icon" style="left:845px;background:#111"><svg width="56" height="56" viewBox="0 0 56 56" fill="none" stroke="#fff" stroke-width="2"><circle cx="14" cy="14" r="6"/><circle cx="42" cy="14" r="6"/><circle cx="14" cy="42" r="6"/><circle cx="42" cy="42" r="6"/><rect x="22" y="22" width="12" height="12"/></svg></div>

<!-- BENEFITS / APPLICATION -->
<div class="abs band-blue"></div>
<div class="abs mid-mark"><span></span></div>
<div class="abs benefit" style="left:163px;top:1958px">
  <div class="kick">BENEFITS OF</div>
  <h3>TRAINING</h3>
  <p>OLU - Bright Reel Studio presents the 5 Benefits of using video for training.</p>
  <ul><li>we understand the importance of engaging and interactive training materials.</li></ul>
  <a class="btn-pill">Watch Video</a>
</div>
<div class="abs benefit" style="left:625px;top:1958px">
  <div class="kick">APPLICATION</div>
  <h3>MARKETING</h3>
  <p>The new video we created for Marco Ruiz Delgado that promotes his APP available for both Droidix &amp; Pomix.</p>
  <ul><li>This will be featured in PlayHub Store &amp; Orchard Store with more than 80.000 Downloads on both platforms.</li></ul>
  <a class="btn-pill">Watch Video</a>
</div>
<div class="abs vid" style="left:162px;background:linear-gradient(135deg,#f0c27a,#e6b066)" role="img" aria-label="Presenter video for training on a warm yellow backdrop"><span class="play"></span></div>
<div class="abs vid" style="left:623px;background:linear-gradient(135deg,#d9d7a8,#c8c690)" role="img" aria-label="Presenter video for app marketing on a pale olive backdrop"><span class="play"></span></div>

<!-- WHY CHOOSE US -->
<div class="abs eyebrow center" style="top:2600px">WHY CHOOSE US</div>
<h2 class="abs h2 center" style="top:2623px">AI's CAPABILITIES IN<br>VIDEO PRODUCTION.</h2>
<div class="abs why-card" style="left:162px">
  <svg width="64" height="64" viewBox="0 0 64 64" fill="none" stroke="#1a6fe8" stroke-width="2"><circle cx="32" cy="34" r="24"/><circle cx="32" cy="34" r="18"/><path d="M32 22v12l8 6M28 6h8"/></svg>
  <h3>Save 80% of Your<br>Time</h3>
  <p>Your human expert in video edition will be working for you autonomously, saving your teams time.</p>
</div>
<div class="abs why-card" style="left:458px">
  <svg width="64" height="64" viewBox="0 0 64 64" fill="none" stroke="#1a6fe8" stroke-width="2"><circle cx="32" cy="24" r="14"/><circle cx="32" cy="24" r="6"/><path d="M32 38v20M24 58h16M32 4v4M12 24h4M48 24h4"/></svg>
  <h3>Save 80% of Your<br>Budget</h3>
  <p>Forget about long and expensive production costs, you will make better quality videos for less money.</p>
</div>
<div class="abs why-card" style="left:756px">
  <svg width="64" height="64" viewBox="0 0 64 64" fill="none" stroke="#1a6fe8" stroke-width="2"><path d="M54 8C40 8 28 18 22 32l10 10c14-6 24-18 22-34z"/><circle cx="42" cy="22" r="5"/><path d="M22 32l-10 2 6-10 10-2M32 42l-2 10 10-6 2-10M10 54l10-10"/></svg>
  <h3>Boost Your Business<br>Efficiency</h3>
  <p style="color:var(--muted)">You can use video to automate different areas of your business such as Marketing, Training &amp; Onboarding.</p>
</div>

<!-- REVIEWS -->
<div class="abs band-review"></div>
<div class="abs eyebrow center" style="top:3233px">TESTIMONIALS</div>
<h2 class="abs h2 center" style="top:3256px">CLIENT REVIEWS</h2>
<div class="abs quote">“</div>
<svg class="abs arrow" style="left:100px;top:3385px" viewBox="0 0 42 20"><path d="M41 10H2M10 2 2 10l8 8" fill="none" stroke="#1a6fe8" stroke-width="2"/></svg>
<svg class="abs arrow" style="left:1057px;top:3385px" viewBox="0 0 42 20"><path d="M1 10h39M32 2l8 8-8 8" fill="none" stroke="#1a6fe8" stroke-width="2"/></svg>
<p class="abs review-text">I only provided screenshots of my app and its main features. Then OLU's creative process kicked in and the result was a great promo video that I uploaded on PlayHub and Orchard Store.</p>
<div class="abs center" style="top:3468px;font-size:16px;font-weight:700">Marco Ruiz Delgado</div>
<div class="abs center" style="top:3495px;font-size:13px;color:var(--body)">Senior Droidix &amp; Pomix Engineer</div>

<!-- BLOG -->
<div class="abs eyebrow center" style="top:3730px">NEWS</div>
<h2 class="abs h2 center" style="top:3752px">RECENT BLOG POSTS</h2>
<div class="abs post" style="left:162px;width:408px;height:323px;background:linear-gradient(135deg,#1c2a48,#3a5278 55%,#1a2238)" role="img" aria-label="Woman with tablet beside a VR headset in a dark office"><span style="font-size:17px">Der Skill Nummer 1 Für Tionen.</span></div>
<div class="abs post" style="left:582px;width:221px;height:268px;background:linear-gradient(160deg,#e8ebee,#a9b2bb 60%,#5a646e)" role="img" aria-label="Person working in a bright modern office"><span>Der Skill Nummer 1 Für<br>Tionen.</span></div>
<div class="abs post" style="left:818px;width:220px;height:268px;background:linear-gradient(160deg,#2b3a55,#4a5b7a 55%,#1a2230)" role="img" aria-label="Trader looking at screens in a dark room"><span>Der Skill Nummer 1 Für<br>Tionen.</span></div>
<svg class="abs arrow" style="left:945px;top:4115px" viewBox="0 0 42 20"><path d="M41 10H2M10 2 2 10l8 8" fill="none" stroke="#1a6fe8" stroke-width="2"/></svg>
<svg class="abs arrow" style="left:998px;top:4115px" viewBox="0 0 42 20"><path d="M1 10h39M32 2l8 8-8 8" fill="none" stroke="#1a6fe8" stroke-width="2"/></svg>

<!-- CONTACT -->
<div class="abs band-foot"></div>
<div class="abs contact-card"><div class="contact-deco"></div></div>
<div class="abs eyebrow" style="left:212px;top:4283px">BOOK A CALL</div>
<h2 class="abs h2" style="left:211px;top:4305px">LET's TALK</h2>
<div class="field" style="left:208px;top:4390px;width:233px;height:43px">First Name<b>*</b></div>
<div class="field" style="left:455px;top:4390px;width:235px;height:43px">Last Name<b>*</b></div>
<div class="field" style="left:208px;top:4450px;width:233px;height:43px">Email<b>*</b></div>
<div class="field" style="left:455px;top:4450px;width:235px;height:43px">Phone<b>*</b></div>
<div class="field" style="left:208px;top:4510px;width:482px;height:110px;border-radius:18px">Message</div>
<a class="abs btn-pill submit">SUBMIT</a>

<!-- FOOTER -->
<div class="abs brand" style="left:490px;top:4795px"><span class="dot"></span>OLU</div>
<nav class="abs foot-nav"><span>Training</span><span>Marketing</span><span>How ?</span><span>Services</span><span>Blogs</span><span>Contact Us</span></nav>
<div class="abs foot-info" style="left:230px">
  <svg width="30" height="34" viewBox="0 0 30 34" fill="none" stroke="#fff" stroke-width="1.6"><path d="M15 32S4 20 4 12a11 11 0 0 1 22 0c0 8-11 20-11 20z"/><circle cx="15" cy="12" r="4"/></svg>
  <div>123, Building Name, Street<br>City, State XY 123456</div>
</div>
<div class="abs foot-info" style="left:545px">
  <svg width="30" height="34" viewBox="0 0 30 34" fill="none" stroke="#fff" stroke-width="1.6"><path d="M7 4l6 6-3 4c2 4 5 7 9 9l4-3 6 6-4 5C14 30 2 18 3 8z"/></svg>
  <div>Call<br>123-456-7890</div>
</div>
<div class="abs foot-info" style="left:777px">
  <svg width="30" height="34" viewBox="0 0 30 34" fill="none" stroke="#fff" stroke-width="1.6"><rect x="3" y="8" width="24" height="20" rx="2"/><path d="M3 10l12 9 12-9"/></svg>
  <div>Email<br>info@brightreel.studio</div>
</div>
<div class="abs rule"></div>
<div class="abs" style="left:163px;top:5068px;color:#fff;font-size:12px">© 2023 BRIGHT REEL STUDIO. All Rights Reserved.</div>
<span class="abs" style="left:987px;top:5066px;width:18px;height:18px;background:#fff;border-radius:3px"></span>
<span class="abs" style="left:1022px;top:5066px;width:18px;height:18px;background:#fff;border-radius:3px"></span>

</body>
</html>
```